New website for salon services and wedding hair and makeup

I am a professional hairstylist and makeup artist in Charleston, SC. I have my own company where I see clients for cut and color and I also go on site for weddings. I have a current website that I would like to update and change the style. I would like to add a contact form, map, additional pages and be mobile friendly. It is important to me that it have a site map and can show up in searches. I will need to add photos to the site every so often and would like to continue to work with the designer. I have a logo that I am happy with and have attached the file however if you think a new logo would help the look of the site I am open to it. My current website is www.brightcurlstudio.example, I would like to change the style and layout so it looks up to date. Here are some links to sites that I like the look of but I don't want to limit your creativity. http://cobaltmeadow.example/ http://www.wovenlensgallery.example http://marenholtby.example/. I have attached a few files for mock up purposes, please let me know if you would like more content. Thank you!

Target Market(s)

Women, Brides

Industry/Entity Type

Hair And Beauty

Number of Pages Required

1 page

Font styles to use
Sans Serif
Script

Requirements
Must have
• Contact form, Mobile friendly, sitemap
Nice to have
• I really like the look for the sites I have included on the project description guide.
Should not have
• Nothing overly girly.

```html
<!DOCTYPE html>
<html lang="en">
<head>
<meta charset="utf-8">
<title>Bright Curl Studio — Hair and Makeup</title>
<link href="https://fonts.googleapis.com/css2?family=Oswald:wght@300;400;500&family=Open+Sans:wght@400;600&display=swap" rel="stylesheet">
<style>
:root{
  --ink:#222;
  --muted:#6b6f73;
  --accent:#d2232a;
  --navy:#163a66;
  --sky:#e3f0f8;
  --sky-deep:#cfe4f2;
  --white:#fff;
  --night:#1b1b1b;
  --field:rgba(255,255,255,.08);
  --field-line:rgba(255,255,255,.45);
  --teal:#8fd3d8;
}
*{box-sizing:border-box;margin:0;padding:0}
html,body{width:1200px;height:3116px;overflow:hidden}
body{font-family:"Open Sans",Arial,sans-serif;color:var(--ink);background:var(--white);position:relative}
.heading{font-family:"Oswald",Arial,sans-serif;text-transform:uppercase;letter-spacing:1px}

/* header */
.topbar{position:absolute;left:0;top:0;width:1200px;height:18px;background:var(--night)}
.site-header{position:absolute;left:0;top:18px;width:1200px;height:112px;background:var(--white);border-bottom:1px solid #ddd}
.brand{position:absolute;left:130px;top:-10px;width:200px;height:170px;display:flex;align-items:center;gap:12px;z-index:3}
.brand-dot{width:18px;height:18px;border-radius:50%;background:var(--teal);flex:none}
.brand-name{font-family:"Oswald",Arial,sans-serif;font-weight:400;font-size:26px;line-height:1.1;color:var(--navy);text-transform:uppercase}
.social{position:absolute;right:140px;top:8px;display:flex;gap:8px}
.social span{width:22px;height:22px;border-radius:3px;background:#3c5a98}
.social span:nth-child(2){background:#2a8fd0}
.social span:nth-child(3){background:#3d6fb0}
.social span:nth-child(4){background:#d04a3a}
.social span:nth-child(5){background:#c4302b}
.main-nav{position:absolute;right:140px;top:82px;display:flex;gap:28px;font-family:"Oswald",Arial,sans-serif;font-size:15px;text-transform:uppercase;color:#555}
.main-nav .current{color:var(--accent)}

/* hero */
.hero{position:absolute;left:0;top:130px;width:1200px;height:510px;background:linear-gradient(100deg,#3a2a20 0%,#6d4c36 40%,#b68a62 62%,#4a3426 100%)}
.hero-title{position:absolute;left:150px;top:145px;color:var(--white);font-weight:400}
.hero-title .lead{display:block;color:var(--accent);font-size:50px;line-height:1.1}
.hero-title .name{display:block;font-size:60px;line-height:1.1;font-weight:300}
.features{position:absolute;left:0;top:640px;width:1200px;height:180px;background:var(--white)}
.feature{position:absolute;top:-180px;width:210px;text-align:center}
.feature-photo{width:200px;height:200px;margin:0 auto;border-radius:50%;border:6px solid var(--white);box-shadow:0 4px 10px rgba(0,0,0,.35)}
.feature-label{margin-top:18px;font-family:"Oswald",Arial,sans-serif;font-size:30px;line-height:1.05;font-weight:500;text-transform:uppercase;color:var(--ink)}
.feature-label small{display:block;font-size:24px;font-weight:400}

/* intro */
.intro{position:absolute;left:0;top:820px;width:1200px;height:380px;background:var(--sky);text-align:center;padding:38px 160px 0}
.intro h2{font-size:24px;font-weight:400;color:var(--ink);margin-bottom:16px}
.intro p{font-size:14px;line-height:1.7;color:var(--muted);margin-bottom:12px}

/* gallery */
.gallery{position:absolute;left:0;top:1200px;width:1200px;height:580px;display:grid;grid-template-columns:repeat(4,300px);grid-template-rows:repeat(2,290px)}
.tile{position:relative}
.tile-label{background:var(--navy);display:flex;flex-direction:column;align-items:center;justify-content:center;color:var(--white);gap:14px}
.tile-label .heading{font-size:28px;font-weight:400}
.tile-caption{position:absolute;left:0;right:0;top:115px;text-align:center;color:var(--white)}
.tile-caption .heading{font-size:20px}
.tile-caption p{font-size:13px}

/* services */
.services{position:absolute;left:0;top:1780px;width:1200px;height:460px;background:linear-gradient(180deg,var(--sky-deep),var(--sky) 60%,#f4f9fc);text-align:center}
.services h2{margin-top:40px;font-size:36px;font-weight:400}
.services .rule{width:60px;height:2px;background:var(--accent);margin:8px auto 16px}
.services .lede{width:820px;margin:0 auto;font-size:14px;line-height:1.7;color:var(--muted)}
.cards{position:absolute;left:175px;top:200px;display:flex;gap:30px}
.card{width:190px;height:180px;background:var(--white);box-shadow:0 2px 6px rgba(0,0,0,.12);padding:44px 14px 0;position:relative}
.card-icon{position:absolute;left:50%;top:-36px;width:54px;height:54px;margin-left:-27px;display:flex;align-items:center;justify-content:center}
.card h3{font-family:"Oswald",Arial,sans-serif;font-size:18px;font-weight:400;color:var(--accent);text-transform:uppercase;margin-bottom:8px}
.card p{font-size:11px;line-height:1.55;color:var(--muted)}
.card .more{display:block;margin-top:10px;font-size:10px;font-weight:600;color:var(--accent);text-transform:uppercase}
.pager{position:absolute;left:0;top:410px;width:1200px;display:flex;justify-content:center;gap:10px}
.pager span{width:28px;height:28px;border-radius:50%;background:#8a8f94}

/* contact */
.contact{position:absolute;left:0;top:2240px;width:1200px;height:720px;background:radial-gradient(ellipse at 55% 25%,#5a5a5a 0%,#2f2f2f 45%,#181818 100%)}
.contact h2{position:absolute;left:0;width:1200px;top:40px;text-align:center;color:var(--white);font-size:36px;font-weight:400}
.contact .rule{position:absolute;left:570px;top:100px;width:60px;height:2px;background:var(--white)}
.field{position:absolute;width:400px;height:50px;border:1px solid var(--field-line);background:var(--field);color:#ddd;font-size:13px;text-transform:uppercase;padding:14px 14px}
.field.address{height:220px}
.send{position:absolute;left:540px;top:530px;width:120px;height:44px;border:1px solid var(--white);color:var(--white);font-family:"Oswald",Arial,sans-serif;font-size:18px;text-transform:uppercase;display:flex;align-items:center;justify-content:center}

/* map + footer */
.map{position:absolute;left:0;top:2960px;width:1200px;height:120px;background:linear-gradient(90deg,#e6e4dc,#d9dcd2 50%,#e9e7df)}
.site-footer{position:absolute;left:0;top:3080px;width:1200px;height:36px;background:var(--night);color:#bbb;font-size:11px;display:flex;align-items:center;justify-content:space-between;padding:0 130px;text-transform:uppercase}
.site-footer nav{display:flex;gap:18px}
</style>
</head>
<body>

<div class="topbar"></div>
<header class="site-header">
  <div class="brand"><span class="brand-dot"></span><span class="brand-name">Bright Curl Studio</span></div>
  <div class="social" aria-label="Social links"><span></span><span></span><span></span><span></span><span></span></div>
  <nav class="main-nav">
    <span class="current">Home</span><span>About Us</span><span>Weddings</span><span>Gallery</span><span>Services</span><span>Contact Us</span>
  </nav>
</header>

<section class="hero" role="img" aria-label="Photo of a woman with long styled hair in warm light">
  <h1 class="hero-title heading"><span class="lead">Welcome to</span><span class="name">Bright Curl Studio</span></h1>
</section>

<section class="features">
  <div class="feature" style="left:150px"><div class="feature-photo" role="img" aria-label="Hair extensions photo" style="background:linear-gradient(135deg,#b07a48,#5a3a22)"></div><div class="feature-label">Hair<small>Extensions</small></div></div>
  <div class="feature" style="left:380px"><div class="feature-photo" role="img" aria-label="Curling irons photo" style="background:linear-gradient(135deg,#d8d8d8,#7a7a7a)"></div><div class="feature-label">Curling<small>Irons</small></div></div>
  <div class="feature" style="left:610px"><div class="feature-photo" role="img" aria-label="Hair coloring photo" style="background:linear-gradient(135deg,#9a9a9a,#3a3a3a)"></div><div class="feature-label">Hair<small>Coloring</small></div></div>
  <div class="feature" style="left:840px"><div class="feature-photo" role="img" aria-label="Blow dryers photo" style="background:linear-gradient(135deg,#e6e6e6,#8c8c8c)"></div><div class="feature-label">Blow<small>Dryers</small></div></div>
</section>

<section class="intro">
  <h2 class="heading">About Us</h2>
  <p>Bright Curl Studio specializes in providing gorgeous, long lasting hair and makeup. With over nine years of experience and training, we know how to make your day the very best. We take pride in client satisfaction and helping you achieve the look of your dreams while making the experience memorable and enjoyable. Our team works on location so you can relax and finish your day with the people you love. We only use the highest quality products, allowing you to dance the night away while your hair and makeup remain flawless. From traditional makeup, airbrush and hair extensions, we will tailor a custom look just for you!</p>
  <p>If your events are of a more professional nature we have you covered! Our team also specializes in airbrush makeup for high definition film, photo shoots, and runway. Our hairstylists specialize in cut, color and extensions giving your client the look they want.</p>
  <p>We provide services in studio and are happy to meet all of your hair care needs.</p>
</section>

<section class="gallery">
  <div class="tile tile-label">
    <svg width="40" height="32" viewBox="0 0 40 32" aria-hidden="true"><rect x="2" y="7" width="36" height="23" rx="3" fill="none" stroke="#fff" stroke-width="2.5"/><rect x="13" y="2" width="14" height="6" fill="#fff"/><circle cx="20" cy="18" r="7" fill="none" stroke="#fff" stroke-width="2.5"/></svg>
    <span class="heading">Photo Gallery</span>
  </div>
  <div class="tile" role="img" aria-label="Woman with red coloured hair" style="background:linear-gradient(160deg,#8a1f1f,#3a1010)">
    <div class="tile-caption"><div class="heading">Hair Coloring</div><p>Bright Curl Studio specialists</p></div>
  </div>
  <div class="tile" role="img" aria-label="Braided updo from behind" style="background:linear-gradient(160deg,#e0c6a8,#9a7656)"></div>
  <div class="tile" role="img" aria-label="Curled bridal updo" style="background:linear-gradient(160deg,#efe6dc,#7a5038)"></div>
  <div class="tile" role="img" aria-label="Long dark wavy hair" style="background:linear-gradient(160deg,#4a3a30,#1e1612)"></div>
  <div class="tile" role="img" aria-label="Side braid hairstyle" style="background:linear-gradient(160deg,#c9a882,#6a4a30)"></div>
  <div class="tile" role="img" aria-label="Auburn bob cut" style="background:linear-gradient(160deg,#a0522d,#4a2414)"></div>
  <div class="tile" role="img" aria-label="Long blonde waves" style="background:linear-gradient(160deg,#f0d69a,#a07a40)"></div>
</section>

<section class="services">
  <h2 class="heading">Our Services</h2>
  <div class="rule"></div>
  <p class="lede">We offer cuts, colour, treatments and extensions in a calm studio setting, plus on site styling for weddings and events. Every service begins with a short consultation so the finished look suits you and lasts all day.</p>
  <div class="cards">
    <div class="card">
      <div class="card-icon"><svg width="40" height="40" viewBox="0 0 40 40" aria-hidden="true"><circle cx="10" cy="30" r="5" fill="none" stroke="#222" stroke-width="2.5"/><circle cx="30" cy="30" r="5" fill="none" stroke="#222" stroke-width="2.5"/><path d="M13 26 L30 4 M27 26 L10 4" stroke="#222" stroke-width="2.5"/></svg></div>
      <h3>Hair Cut</h3><p>Precision cuts shaped to your face, texture and daily routine, finished with a blow dry.</p><span class="more">Read More</span>
    </div>
    <div class="card">
      <div class="card-icon"><svg width="40" height="40" viewBox="0 0 40 40" aria-hidden="true"><path d="M20 4 C12 16 10 22 10 27 a10 10 0 0 0 20 0 C30 22 28 16 20 4Z" fill="#222"/></svg></div>
      <h3>Hair Color</h3><p>Soft highlights, rich glosses and full colour, blended by hand for a natural finish.</p><span class="more">Read More</span>
    </div>
    <div class="card">
      <div class="card-icon"><svg width="40" height="40" viewBox="0 0 40 40" aria-hidden="true"><path d="M20 3 L24 16 L37 20 L24 24 L20 37 L16 24 L3 20 L16 16Z" fill="#222"/></svg></div>
      <h3>Treatments</h3><p>Deep conditioning and repair treatments that restore shine, softness and strength.</p><span class="more">Read More</span>
    </div>
    <div class="card">
      <div class="card-icon"><svg width="40" height="40" viewBox="0 0 40 40" aria-hidden="true"><path d="M10 4 C6 16 14 24 10 36 M20 4 C16 16 24 24 20 36 M30 4 C26 16 34 24 30 36" fill="none" stroke="#222" stroke-width="2.5"/></svg></div>
      <h3>Hair Extensions</h3><p>Quality extensions fitted for added length and volume that blend with your own hair.</p><span class="more">Read More</span>
    </div>
  </div>
  <div class="pager"><span></span><span></span></div>
</section>

<section class="contact" role="img" aria-label="Dark backdrop photo of flowing hair">
  <h2 class="heading">Contact Us</h2>
  <div class="rule"></div>
  <div class="field" style="left:185px;top:130px">Your Name</div>
  <div class="field" style="left:615px;top:130px">Email Address</div>
  <div class="field" style="left:185px;top:200px">Mobile No.</div>
  <div class="field" style="left:615px;top:200px">Address</div>
  <div class="field address" style="left:185px;top:270px;width:830px">Address</div>
  <div class="send">Send</div>
</section>

<div class="map" role="img" aria-label="Street map showing the studio location"></div>

<footer class="site-footer">
  <nav><span>Home</span><span>About Us</span><span>Weddings</span><span>Gallery</span><span>Services</span><span>Contact Us</span></nav>
  <span>Copyright www.brightcurlstudio.example All Rights Reserved</span>
</footer>

</body>
</html>
```